Brand & packaging design for joy-ful nutritional drink

I would like to design packaging for a happy, mood balancing nutritional drink. The product is called "Brisko", and the brand identity is about joy & happiness.

The product is a nutritional drink filled with vitamins, minerals, and superfoods that enable optimal brain health and energy. The drink comes in a bottle, about 350ml in size. Please design the bottle and packaging, including logo, color schemes, shape and size of bottle (as you see fit), etc. Please be creative, and make sure that the design reflects the brand identity of happiness.

Entries with simple designs, and happy / joyous format will be favored -- something that makes you happy and excited to look at.

For inspiration, you can look at similar products: Qel, Lumen Brew, and Porla tea. Images of these products are attached for reference.

```html
<!DOCTYPE html>
<html lang="en">
<head>
<meta charset="utf-8">
<title>Brisko – joy &amp; happiness label</title>
<link rel="stylesheet" href="https://fonts.googleapis.com/css2?family=Arimo:wght@400;700&display=swap">
<style>
  :root {
    --backdrop: #c9c9c9;
    --label-white: #ffffff;
    --brand-blue: #1f3f9a;
    --joy-red: #d8262b;
    --tag-ink: #1e3a48;
    --band-yellow: #f4e51c;
    --lime: #d6ec6a;
    --mint: #bfe3d6;
    --lotus: #f08a80;
  }
  * { margin: 0; padding: 0; box-sizing: border-box; }
  html, body {
    width: 1200px;
    height: 1185px;
    overflow: hidden;
    background: var(--backdrop);
    font-family: "Arimo", Arial, sans-serif;
  }
  .label {
    position: absolute;
    left: 204px;
    top: 53px;
    width: 792px;
    height: 1079px;
    background: var(--label-white);
    overflow: hidden;
  }
  .label__pattern {
    position: absolute;
    left: 0;
    top: 0;
    width: 500px;
    height: 960px;
    background:
      radial-gradient(ellipse at 35% 50%, var(--lime) 0%, rgba(214,236,106,0.5) 40%, rgba(255,255,255,0) 72%),
      radial-gradient(ellipse at 75% 12%, var(--mint) 0%, rgba(191,227,214,0) 55%);
  }
  .brand-name {
    position: absolute;
    left: 80px;
    top: 150px;
    font-weight: 700;
    font-size: 130px;
    line-height: 1;
    color: var(--brand-blue);
    letter-spacing: 2px;
  }
  .brand-line {
    position: absolute;
    right: 60px;
    font-weight: 400;
    font-size: 56px;
    line-height: 1;
    color: var(--joy-red);
    text-align: right;
  }
  .brand-line--joy { top: 262px; }
  .brand-line--happy { top: 322px; }
  .label__lotus {
    position: absolute;
    left: 150px;
    top: 450px;
    width: 500px;
    height: 230px;
  }
  .tagline {
    position: absolute;
    right: 60px;
    top: 760px;
    text-align: right;
    font-size: 54px;
    line-height: 62px;
    color: var(--tag-ink);
  }
  .label__band {
    position: absolute;
    left: 0;
    top: 962px;
    width: 100%;
    height: 32px;
    background: var(--band-yellow);
  }
</style>
</head>
<body>
  <div class="label">
    <div class="label__pattern" role="img" aria-label="Decorative pattern of soft lime and mint translucent squares"></div>

    <div class="brand-name">BRISKO</div>
    <div class="brand-line brand-line--joy">joy &amp;</div>
    <div class="brand-line brand-line--happy">happiness</div>

    <svg class="label__lotus" viewBox="0 0 500 230" role="img" aria-label="Illustration of a pink lotus flower">
      <defs>
        <radialGradient id="lotusGlow" cx="50%" cy="65%" r="50%">
          <stop offset="0%" stop-color="#f08a80" stop-opacity="0.85"/>
          <stop offset="100%" stop-color="#f08a80" stop-opacity="0"/>
        </radialGradient>
      </defs>
      <rect width="500" height="230" fill="url(#lotusGlow)"/>
    </svg>

    <div class="tagline">happy &amp;<br>mood balancing<br>nutritional drink</div>

    <div class="label__band"></div>
  </div>
</body>
</html>
```